Bellvane Movement Troupe needs an A-frame sign design

Bellvane Movement Troupe needs an A-frame sign for placing on the street outside of our dance studio. We are a dance school with a difference, offering recreational dance classes in various styles including contemporary, hip hop, ballet, jazz and capoeira as well as performance opportunities. We also are Creative Arts Therapists specialising in Dance Movement Therapy. I would like to see a design that incorporates our logo and lists the services we have, as well as our contact information (phone number and email address). I want the design to be not too busy, is bold and has a professional, clean quality to it, potentially utilising the three colours in our logo design. I'm interested in seeing two designs; one without any images of people and one that incorporates a photo.
Target Market(s)
Families with children, adults interested in dance
Requirements
Must have
- Logo, list all of our dance styles and the text 'Creative Art Therapy - QPHV Registered'

```html
<!DOCTYPE html>
<html lang="en">
<head>
<meta charset="utf-8">
<title>Bellvane Movement Troupe – A-Frame Sign</title>
<link href="https://fonts.googleapis.com/css2?family=Poppins:wght@400;500;600;700;800&display=swap" rel="stylesheet">
<style>
  :root {
    --brand-blue: #1371bd;
    --deep-blue: #1d63b4;
    --sky: #62c6de;
    --green: #3db54a;
    --green-dark: #2f9a3c;
    --navy: #202a68;
    --ink: #111111;
    --grey-text: #3c3c3c;
    --badge: #6a2a7e;
    --white: #ffffff;
  }
  * { margin: 0; padding: 0; box-sizing: border-box; }
  html, body { width: 866px; height: 1200px; overflow: hidden; background: var(--white); }
  .sign {
    position: relative;
    width: 866px;
    height: 1200px;
    overflow: hidden;
    font-family: "Poppins", sans-serif;
    background: linear-gradient(180deg, #f4f4f4 0%, #ffffff 35%, #ffffff 100%);
  }
  .backdrop { position: absolute; inset: 0; }

  .brand {
    position: absolute;
    top: 66px;
    left: 163px;
    display: flex;
    align-items: center;
    height: 152px;
  }
  .brand-square {
    width: 150px;
    height: 150px;
    background: var(--brand-blue);
  }
  .brand-divider {
    width: 2px;
    height: 150px;
    margin: 0 26px 0 24px;
    background: #e2e2e2;
  }
  .brand-name {
    color: var(--ink);
    font-weight: 800;
    font-size: 47px;
    line-height: 52px;
    letter-spacing: 0.5px;
    text-transform: uppercase;
  }

  .styles {
    position: absolute;
    top: 285px;
    left: 0;
    width: 866px;
    list-style: none;
    text-align: center;
  }
  .styles li {
    position: relative;
    height: 104px;
    line-height: 100px;
    color: var(--brand-blue);
    font-weight: 700;
    font-size: 74px;
    letter-spacing: -1px;
  }
  .styles li:not(:last-child)::after {
    content: "";
    position: absolute;
    left: 80px;
    right: 80px;
    bottom: 0;
    height: 6px;
    background: radial-gradient(ellipse at center, rgba(0,0,0,0.10) 0%, rgba(0,0,0,0) 70%);
  }

  .waves { position: absolute; left: 0; top: 740px; }

  .therapy {
    position: absolute;
    right: 396px;
    top: 800px;
    text-align: right;
    color: var(--grey-text);
    font-size: 24px;
    line-height: 32px;
    font-weight: 400;
  }

  .badge {
    position: absolute;
    left: 503px;
    top: 742px;
    width: 244px;
    height: 244px;
    border-radius: 50%;
    background: var(--white);
    box-shadow: 0 6px 16px rgba(0,0,0,0.25);
  }
  .badge::after {
    content: "";
    position: absolute;
    inset: 14px;
    border-radius: 50%;
    background: var(--badge);
  }

  .contact {
    position: absolute;
    left: 0;
    top: 1030px;
    width: 866px;
    text-align: center;
  }
  .email {
    color: var(--white);
    font-size: 37px;
    font-weight: 500;
    line-height: 50px;
  }
  .call {
    position: relative;
    margin: 16px auto 0 149px;
    width: 575px;
    height: 58px;
    border-radius: 29px;
    background: var(--green);
    color: var(--white);
    display: flex;
    align-items: center;
    padding-left: 82px;
    font-size: 47px;
    line-height: 58px;
  }
  .call-icon {
    position: absolute;
    left: 2px;
    top: 1px;
    width: 60px;
    height: 56px;
  }
  .call-label { font-weight: 500; margin-right: 14px; }
  .call-number { font-weight: 700; }
</style>
</head>
<body>
<main class="sign">
  <svg class="backdrop" width="866" height="1200" viewBox="0 0 866 1200" aria-hidden="true">
    <polygon points="60,0 160,0 420,380 330,380" fill="#ffffff" opacity="0.8"/>
    <polygon points="706,0 806,0 536,380 446,380" fill="#ffffff" opacity="0.8"/>
    <polygon points="0,220 0,300 200,520 250,520" fill="#eeeeee" opacity="0.6"/>
    <polygon points="866,220 866,300 666,520 616,520" fill="#eeeeee" opacity="0.6"/>
  </svg>

  <header class="brand">
    <div class="brand-square"></div>
    <div class="brand-divider"></div>
    <div class="brand-name">Bellvane<br>Movement<br>Troupe</div>
  </header>

  <ul class="styles">
    <li>CONTEMPORARY</li>
    <li>HIP HOP, BALLET</li>
    <li>JAZZ AND</li>
    <li>CAPOEIRA</li>
  </ul>

  <svg class="waves" width="866" height="460" viewBox="0 740 866 460" aria-hidden="true">
    <path d="M0,787 C170,850 380,905 560,905 C690,905 790,870 866,838 L866,1200 L0,1200 Z" fill="var(--deep-blue)"/>
    <path d="M560,915 C690,900 790,850 866,780 L866,808 C790,870 690,920 560,935 Z" fill="var(--green)"/>
    <path d="M560,942 C690,930 790,890 866,835 L866,850 C790,905 690,945 560,955 Z" fill="var(--sky)"/>
    <path d="M0,830 C150,880 320,920 480,930 C300,925 140,895 0,858 Z" fill="#2b86d6"/>
    <path d="M0,880 C140,925 280,950 420,955 C270,960 130,945 0,915 Z" fill="var(--sky)"/>
    <path d="M0,948 C220,965 480,975 866,925 L866,1200 L0,1200 Z" fill="var(--navy)"/>
  </svg>

  <p class="therapy">Creative Art Therapy -<br>QPHV Registered</p>

  <div class="badge" role="img" aria-label="Registration badge"></div>

  <section class="contact">
    <p class="email">info@bellvanetroupe.com</p>
    <p class="call">
      <svg class="call-icon" viewBox="0 0 60 56" aria-hidden="true">
        <circle cx="28" cy="28" r="27" fill="var(--green-dark)"/>
        <circle cx="28" cy="28" r="20" fill="var(--white)"/>
        <path d="M20,18 l5,-2 l3,7 l-3,2 c1,4 4,7 8,8 l2,-3 l7,3 l-2,5 c-12,1 -21,-8 -20,-20 Z" fill="var(--green)"/>
      </svg>
      <span class="call-label">Call</span><span class="call-number">1800 XX XXX</span>
    </p>
  </section>
</main>
</body>
</html>
```